create a book cover titled "bright canyon drift"

>>>>Updated Description>>>>>
I need conceptually enriched and minimal book cover design that hopefully represents the theme on the front page, The book is about romanticizing greenery and forests. It's a novel based on life of botanical creatures and their interaction. Think of it as a role playing novel where you(the reader) will be experiencing the story and life of botany. Book is also accompanied by a series of soundtracks which will be embedded through some secondary medium within the book.
- The cover should be simple and very minimal and could be orignal illustration
- Only design front cover, inner content and back cover design details will be shared with the winning designer only.
- Don't do any ornamanation
- It should be very too the point and clean
- hit me up incase of any confusions and ask me to clarify anything, I am here to help you out,feel free to post but design isn't really my thing so you've 100% creative freedom, I just want the design of the book cover to represent my ideas visually.
- dimensions 5.5x8

Please view the updated brief. Please alter your designs accordingly. Best Regards

Target Market(s)

adults

Font styles to use
Serif
Sans Serif

Colors

Designer to choose colors to be used in the design.

Requirements
Must have
• - Minimal design
• - Clean text
• - Bold Imagery
Nice to have
• Illustrations
Should not have
• - Dark colors
• - something abstract
• - Contentless elements

```html
<!DOCTYPE html>
<html lang="en">
<head>
<meta charset="utf-8">
<title>Bright Canyon Drift – Book Cover</title>
<link rel="stylesheet" href="https://fonts.googleapis.com/css2?family=Bangers&family=Oswald:wght@700&family=Open+Sans:wght@400&display=swap">
<style>
  :root {
    --page-bg: #e8e2da;
    --ink-white: #ffffff;
    --label-ink: #2a2520;
    --spine-seam: #c9a46a;
    --canopy-dark: #1f3322;
    --canopy-mid: #3f5a3a;
    --mist: #c9d3cf;
    --path-grey: #7d7a86;
    --path-brown: #4a3f3c;
  }
  * { margin: 0; padding: 0; box-sizing: border-box; }
  html, body {
    width: 1200px; height: 800px; overflow: hidden;
    background: var(--page-bg);
  }
  .canvas { position: relative; width: 1200px; height: 800px; }

  .book-flat {
    position: absolute; left: 325px; top: 40px;
    width: 551px; height: 680px;
  }
  .forest-art {
    position: absolute; inset: 0;
    background:
      radial-gradient(ellipse 55% 22% at 55% 56%, rgba(226,232,228,0.85), rgba(226,232,228,0) 100%),
      linear-gradient(180deg,
        var(--canopy-dark) 0%,
        var(--canopy-mid) 30%,
        #6f8470 48%,
        var(--mist) 58%,
        var(--path-grey) 74%,
        var(--path-brown) 100%);
  }
  .spine-seam {
    position: absolute; left: 87px; top: 0; width: 1px; height: 100%;
    background: var(--spine-seam);
  }

  .spine { position: absolute; left: 0; top: 0; width: 87px; height: 100%; }
  .spine-title {
    position: absolute; left: 24px; top: 56px;
    writing-mode: vertical-rl;
    font-family: "Oswald", sans-serif; font-weight: 700;
    font-size: 31px; letter-spacing: 0.5px;
    color: var(--ink-white); text-transform: uppercase;
  }
  .spine-author {
    position: absolute; left: 28px; top: 440px;
    writing-mode: vertical-rl;
    font-family: "Bangers", cursive;
    font-size: 26px; letter-spacing: 1px;
    color: var(--ink-white);
  }

  .front-cover { position: absolute; left: 88px; top: 0; width: 463px; height: 100%; }
  .cover-author {
    position: absolute; top: 68px; left: 0; width: 100%;
    text-align: center;
    font-family: "Bangers", cursive;
    font-size: 36px; letter-spacing: 1px;
    color: var(--ink-white);
  }
  .cover-title { position: absolute; inset: 0; }
  .cover-title text {
    font-family: "Oswald", sans-serif; font-weight: 700;
    fill: var(--ink-white);
  }

  .caption {
    position: absolute; top: 730px;
    font-family: "Open Sans", sans-serif; font-size: 15px;
    letter-spacing: 1.5px; color: var(--label-ink);
  }
  .caption-spine { left: 346px; }
  .caption-front { left: 608px; }
  .caption-rule {
    position: absolute; left: 413px; top: 723px;
    width: 463px; height: 1px; background: var(--label-ink);
  }
</style>
</head>
<body>
<main class="canvas">
  <section class="book-flat">
    <div class="forest-art" role="img" aria-label="Sunlit forest path between tall trees with soft mist and light rays"></div>
    <div class="spine-seam"></div>

    <div class="spine">
      <div class="spine-title">Bright Canyon Drift</div>
      <div class="spine-author">AUTHOR NAME</div>
    </div>

    <div class="front-cover">
      <div class="cover-author">AUTHOR NAME</div>
      <svg class="cover-title" viewBox="0 0 463 680" width="463" height="680" aria-label="Bright Canyon Drift">
        <defs>
          <path id="title-curve" d="M142,588 Q285,566 440,468"/>
        </defs>
        <text x="32" y="588" font-size="200" textLength="98" lengthAdjust="spacingAndGlyphs">B</text>
        <text font-size="90">
          <textPath href="#title-curve" textLength="300" lengthAdjust="spacingAndGlyphs"><tspan font-size="92">R</tspan><tspan font-size="86">I</tspan><tspan font-size="80">G</tspan><tspan font-size="74">H</tspan><tspan font-size="68">T</tspan><tspan font-size="36"> </tspan><tspan font-size="54">C</tspan><tspan font-size="50">A</tspan><tspan font-size="47">N</tspan><tspan font-size="44">Y</tspan><tspan font-size="42">O</tspan><tspan font-size="40">N</tspan><tspan font-size="28"> </tspan><tspan font-size="36">D</tspan><tspan font-size="34">R</tspan><tspan font-size="32">I</tspan><tspan font-size="30">F</tspan><tspan font-size="29">T</tspan></textPath>
        </text>
      </svg>
    </div>
  </section>

  <div class="caption-rule"></div>
  <div class="caption caption-spine">Spine</div>
  <div class="caption caption-front">Front Cover</div>
</main>
</body>
</html>
```